Splashtide Cove and Phase 3 Now Open - The Lodge @ Cedarbrook Hollow

A email that features that the addition to our outdoor waterpark - Splashtide Cove is now open and 67 brand new rooms in our phase 3 building is open. This needs to be fun and inviting and grasp attention and want people to visit the waterpark. Will be using Constant Contact to send to email list so needs to be formatted correctly.

Target Market(s)

Guest who have and have not visited The Lodge

Industry/Entity Type

Hospitality

Requirements
Must have
• a Reserve Now call to action
• phone number 800.555.0173
• website https://www.lodgeatcedarbrookhollow.example/
• hashtag #lodgech #happytripalways
Nice to have
• Modern, vibrant fun design. Do not have to use all pictures attached but should use the best ones to promote fun and luxury accommodations.
Should not have
• we are in the SMoky Mountains in Pigeon Forge Tennessee so no references to beaches, etc.

```html
<!DOCTYPE html>
<html lang="en">
<head>
<meta charset="utf-8">
<title>Splashtide Cove Now Open – The Lodge @ Cedarbrook Hollow</title>
<link rel="stylesheet" href="https://fonts.googleapis.com/css2?family=Playfair+Display:wght@400;700&family=Italianno&display=swap">
<style>
  :root {
    --teal: #5a7f85;
    --teal-text: #5f7f86;
    --cream: #fdf6e8;
    --brown: #5a3a25;
    --white: #ffffff;
    --hash: #bdbdbd;
    --ink: #4e4e4e;
    --caption: rgba(78, 116, 122, 0.84);
  }
  * { margin: 0; padding: 0; box-sizing: border-box; }
  html, body { width: 1200px; height: 2884px; overflow: hidden; background: var(--white); }
  body { position: relative; font-family: "Playfair Display", Georgia, serif; font-variant-numeric: lining-nums; }
  .abs { position: absolute; }
  .center { left: 0; width: 1200px; text-align: center; }

  .top-bar { top: 0; left: 0; width: 1200px; height: 156px; background: var(--teal); }
  .phone { top: 56px; left: 44px; color: var(--white); font-size: 35px; letter-spacing: 0.5px; }
  .brand { top: 38px; color: var(--white); font-size: 66px; font-weight: 700; }
  .social { display: flex; gap: 8px; }
  .social span { display: block; border-radius: 50%; }
  .social-top { top: 44px; left: 840px; }
  .social-top span { width: 72px; height: 72px; border: 3px solid var(--white); background: rgba(255,255,255,0.12); }

  .features { top: 156px; left: 0; width: 1200px; height: 986px; background: var(--cream); }
  .headline { top: 346px; font-size: 58px; font-weight: 400; color: var(--brown); }
  .feature-name { font-size: 35px; font-weight: 700; color: var(--brown); }
  .feature-copy { font-size: 34px; color: var(--teal-text); line-height: 48px; }
  .feature-a { top: 438px; }
  .feature-b { top: 598px; }

  .thumb { top: 754px; width: 272px; height: 272px; border-radius: 50%; }
  .thumb-living { left: 40px;
    background: linear-gradient(160deg, #c9b79a 0%, #9c7f5e 35%, #4a3426 65%, #2e221c 100%); }
  .thumb-splash-a { left: 322px;
    background: linear-gradient(180deg, #8cc4ec 0%, #4d93d6 45%, #f0c84a 60%, #3b8fd9 75%, #2a6fc0 100%); }
  .thumb-kitchen { left: 604px;
    background: linear-gradient(150deg, #3a2a22 0%, #6b5444 40%, #b7a48c 70%, #8d7a66 100%); }
  .thumb-splash-b { left: 884px;
    background: linear-gradient(200deg, #e9f4fc 0%, #5aa6e6 30%, #1f6fc6 60%, #7cc24a 85%, #2b6bb8 100%); }

  .hero { top: 1142px; left: 0; width: 1200px; height: 788px;
    background:
      linear-gradient(90deg, rgba(214,150,70,0.55) 0%, rgba(214,150,70,0) 35%, rgba(214,150,70,0) 55%, rgba(226,160,80,0.6) 100%),
      linear-gradient(180deg, #3a4c97 0%, #5668a8 28%, #6f7fae 40%, #c39456 52%, #a5855a 62%, #58b7c2 74%, #47616a 84%, #39474c 100%); }
  .hero-caption { top: 1754px; left: 0; width: 1200px; height: 176px; background: var(--caption);
    color: var(--white); font-size: 51px; font-weight: 700; line-height: 66px; text-align: center; padding-top: 20px; }

  .btn { background: var(--teal); color: var(--white); font-weight: 700; text-align: center; }
  .btn-small { top: 1098px; left: 426px; width: 332px; height: 88px; border: 3px solid var(--white);
    border-radius: 44px; font-size: 31px; line-height: 82px; }
  .btn-large { top: 2306px; left: 352px; width: 502px; height: 132px; border-radius: 66px;
    font-size: 58px; line-height: 132px; }

  .season { top: 1978px; font-size: 50px; color: var(--teal-text); line-height: 64px; }
  .start { top: 2120px; font-family: "Italianno", cursive; font-size: 172px; color: var(--teal-text);
    line-height: 160px; -webkit-text-stroke: 2px var(--teal-text); }
  .hashtags { top: 2466px; font-size: 30px; color: var(--hash); word-spacing: 8px; }
  .contact-label { top: 2566px; font-size: 30px; color: var(--teal-text); }
  .social-bottom { top: 2624px; left: 440px; gap: 10px; }
  .social-bottom span { width: 72px; height: 72px; border: 3px solid var(--teal); }
  .visit-label { top: 2746px; font-size: 30px; color: var(--ink); }
  .site-url { top: 2790px; font-size: 31px; color: var(--ink); }
</style>
</head>
<body>
  <header>
    <div class="abs top-bar"></div>
    <div class="abs phone">1-800-555-0173</div>
    <div class="abs center brand">The Lodge</div>
    <div class="abs social social-top"><span></span><span></span><span></span><span></span></div>
  </header>

  <section>
    <div class="abs features"></div>
    <h1 class="abs center headline">67 More Fully Furnished Condos!</h1>
    <div class="abs center feature-a">
      <div class="feature-name">GLOWBERRY GROVE:</div>
      <div class="feature-copy">Featuring Firepits,<br>Hammock Area &amp; Picnic Grounds</div>
    </div>
    <div class="abs center feature-b">
      <div class="feature-name">SPLASHTIDE COVE:</div>
      <div class="feature-copy">Outdoor Children’s Waterplay Area</div>
    </div>
    <div class="abs thumb thumb-living" role="img" aria-label="Condo living room with TV and sofa"></div>
    <div class="abs thumb thumb-splash-a" role="img" aria-label="Children's water play structure with spray features"></div>
    <div class="abs thumb thumb-kitchen" role="img" aria-label="Condo kitchen with granite counter and sink"></div>
    <div class="abs thumb thumb-splash-b" role="img" aria-label="Water play tower splashing under blue sky"></div>
  </section>

  <section>
    <div class="abs hero" role="img" aria-label="Lodge buildings at dusk surrounding the outdoor pool and water slides"></div>
    <div class="abs btn btn-small">RESERVE NOW</div>
    <div class="abs hero-caption">Travelers have been visiting The Great Smoky<br>Mountains of East Tennessee for decades.</div>
  </section>

  <section>
    <div class="abs center season">Our 2018 season will end on Jan. 5, 2019<br>&amp; the 2019 season will</div>
    <div class="abs center start">Start March 8th</div>
    <div class="abs btn btn-large">RESERVE NOW</div>
    <div class="abs center hashtags">#lodgech #happytripalways</div>
  </section>

  <footer>
    <div class="abs center contact-label">GET IN TOUCH</div>
    <div class="abs social social-bottom"><span></span><span></span><span></span><span></span></div>
    <div class="abs center visit-label">VISIT US ON</div>
    <div class="abs center site-url">www.lodgeatcedarbrookhollow.example</div>
  </footer>
</body>
</html>
```